Anzeigengestaltung für Handwerksbetrieb
Zielgruppe
Handwerksbetrieb
Maler und Lackierer
Wir möchten mit einem auffälligem und einprägsamen Werbeslogen unsere Bekanntheit in unserer Stadt verstärken. Dieses Design samt Slogan soll künftig alle unsere Werbeaktionen begleiten.
Aufgabenstellung
Der Werbeslogan : 'Wir machen Braunschweig bunter' muss enthalten sein.
Ein optischer Zusammenhang zur Stadt Braunschweig wie z.B. Silouette der Stadt wären wünschenswert.
Gerne bunt und auffallend gestaltet.

```html
<!DOCTYPE html>
<html lang="de">
<head>
<meta charset="utf-8">
<title>Kellbrand Malerbetrieb – Wir machen Braunschweig bunter</title>
<link rel="stylesheet" href="https://fonts.googleapis.com/css2?family=Playfair+Display:wght@700;800&family=Montserrat:wght@700&display=swap">
<style>
  :root {
    --ink: #000000;
    --paper: #ffffff;
    --wine: #7d1a22;
    --gold: #d6bf86;
    --logo-gold: #b89a5e;
    --sky-violet: #4a3a8c;
    --sky-orange: #e2702c;
    --sky-teal: #2f8f8a;
    --sky-magenta: #8a2f7a;
  }
  html, body {
    margin: 0;
    width: 1200px;
    height: 1200px;
    overflow: hidden;
    background: var(--paper);
  }
  .ad {
    position: relative;
    width: 1200px;
    height: 1200px;
    overflow: hidden;
    background: var(--ink);
  }
  .skyline {
    position: absolute;
    left: 0; top: 0;
    width: 1200px; height: 700px;
    background:
      linear-gradient(to bottom, rgba(0,0,0,0) 70%, var(--ink) 100%),
      radial-gradient(ellipse at 20% 80%, var(--sky-orange) 0%, rgba(226,112,44,0) 40%),
      radial-gradient(ellipse at 70% 50%, var(--sky-teal) 0%, rgba(47,143,138,0) 40%),
      radial-gradient(ellipse at 85% 35%, var(--sky-orange) 0%, rgba(226,112,44,0) 30%),
      linear-gradient(to bottom, #f4f0f4 0%, var(--sky-violet) 55%, var(--sky-magenta) 85%);
  }
  .header-sheet {
    position: absolute;
    left: 0; top: 0;
  }
  .brand {
    position: absolute;
    left: 40px; top: 220px;
    width: 400px;
    text-align: center;
    font-family: "Playfair Display", Georgia, serif;
    font-weight: 700;
    font-size: 40px;
    line-height: 1.15;
    color: var(--logo-gold);
    margin: 0;
  }
  .slogan {
    position: absolute;
    left: 0; top: 700px;
    width: 1200px; height: 380px;
    margin: 0;
    text-align: center;
    font-family: "Playfair Display", Georgia, serif;
    font-weight: 800;
    color: var(--paper);
  }
  .slogan .line { display: block; }
  .slogan .line-top { font-size: 82px; line-height: 1; padding-top: 30px; }
  .slogan .line-city { font-size: 118px; line-height: 1.05; color: var(--gold); padding-top: 12px; }
  .slogan .line-bottom { font-size: 82px; line-height: 1; padding-top: 12px; }
  .contact-bar {
    position: absolute;
    left: 0; top: 1080px;
    width: 1200px; height: 120px;
    background: var(--wine);
    display: flex;
    align-items: center;
    justify-content: center;
    gap: 36px;
    font-family: "Montserrat", Arial, sans-serif;
    font-weight: 700;
    font-size: 22px;
    color: var(--paper);
  }
  .contact-item { display: flex; align-items: center; gap: 14px; }
  .contact-dot {
    width: 34px; height: 34px;
    border-radius: 50%;
    background: var(--paper);
  }
</style>
</head>
<body>
<main class="ad">
  <div class="skyline" role="img" aria-label="Bunte Aquarell-Silhouette einer Stadt mit Türmen und Hochhäusern"></div>

  <svg class="header-sheet" width="1200" height="700" viewBox="0 0 1200 700" aria-hidden="true">
    <path d="M0 0 H760 C650 0 620 110 570 260 C525 390 450 425 360 425 H0 Z" fill="var(--paper)"/>
    <path d="M760 0 C650 0 620 110 570 260 C525 390 450 425 360 425" fill="none" stroke="var(--wine)" stroke-width="12"/>
    <line x1="30" y1="425" x2="360" y2="425" stroke="#cfcfcf" stroke-width="1.5"/>
  </svg>

  <p class="brand">Kellbrand<br>Malerbetrieb</p>

  <h1 class="slogan">
    <span class="line line-top">Wir machen</span>
    <span class="line line-city">BRAUNSCHWEIG</span>
    <span class="line line-bottom">bunter</span>
  </h1>

  <footer class="contact-bar">
    <div class="contact-item"><span class="contact-dot"></span>www.malerbetrieb-kellbrand.example</div>
    <div class="contact-item"><span class="contact-dot"></span>social.example/malerbetriebkellbrand/</div>
  </footer>
</main>
</body>
</html>
```